Need a professional looking Consulting site for Consulting Services Company

Stock professional office images with a registration page for contact

Coding

Coded - Design and coding required

```html
<!DOCTYPE html>
<html lang="en">
<head>
<meta charset="utf-8">
<title>Greenmore Consulting</title>
<link href="https://fonts.googleapis.com/css2?family=Roboto:wght@400;500;700&family=Open+Sans:wght@400;600;700&display=swap" rel="stylesheet">
<style>
:root{
  --green:#2e9a44;
  --green-dark:#23803a;
  --ink:#1c1c1c;
  --text:#555;
  --light:#f4f5f4;
  --white:#fff;
  --line:#e2e2e2;
}
*{box-sizing:border-box;margin:0;padding:0}
html,body{width:1200px;height:5017px;overflow:hidden}
body{position:relative;font-family:"Open Sans",Arial,sans-serif;color:var(--text);background:var(--white)}
.abs{position:absolute}
.heading{font-family:"Roboto",Arial,sans-serif;font-weight:400;color:var(--ink);text-align:center;letter-spacing:.5px}
.section-title{font-size:40px;left:0;width:1200px}
.underline{height:4px;width:84px;background:var(--green);left:558px}
.btn-outline{border:2px solid var(--green);color:var(--green);border-radius:24px;font-weight:700;font-size:14px;text-align:center;letter-spacing:.5px;background:var(--white)}
.btn-solid{background:var(--green);color:var(--white);border-radius:24px;font-weight:700;font-size:15px;text-align:center;font-family:"Roboto",Arial,sans-serif}

/* top bar */
.topbar{left:0;top:0;width:1200px;height:39px;background:var(--green);color:var(--white);font-size:13px}
.topbar .social{top:11px;width:16px;height:16px;border-radius:50%;background:rgba(255,255,255,.85)}
.topbar .info{top:11px}
.topbar .divider{top:0;width:1px;height:39px;background:rgba(255,255,255,.4)}

/* header */
.header{left:0;top:39px;width:1200px;height:82px;background:var(--white)}
.brand{font-family:"Roboto",Arial,sans-serif;font-weight:500;color:var(--green);font-size:38px}
.brand-dot{width:18px;height:18px;border-radius:50%;background:var(--green)}
.nav a{position:absolute;top:32px;font-family:"Roboto",Arial,sans-serif;font-size:14px;color:var(--ink);text-decoration:none;font-weight:500}
.nav a.active{color:var(--green)}

/* hero */
.hero{left:0;top:121px;width:1200px;height:594px;background:linear-gradient(100deg,#7d8c99 0%,#c9c4bb 35%,#b8b0a4 60%,#5e6670 100%)}
.hero-title{font-size:72px;top:60px;left:0;width:1200px;color:#111}
.hero-sub{top:150px;left:0;width:1200px;text-align:center;font-size:17px;color:#111;line-height:26px}
.dot{width:11px;height:11px;border-radius:50%;border:2px solid var(--white)}

/* services */
.service{width:240px;text-align:center}
.service .ring{width:162px;height:162px;border-radius:50%;border:4px solid var(--green);margin:0 auto;position:relative}
.service .core{position:absolute;left:10px;top:10px;width:134px;height:134px;border-radius:50%;background:var(--green)}
.service h3{font-family:"Roboto",Arial,sans-serif;font-size:17px;color:var(--ink);font-weight:500;margin-top:28px}
.service p{font-size:13px;line-height:21.5px;margin:10px 18px 0;color:#666}

/* industry */
.tile{width:294px;height:329px;overflow:hidden}
.tile .photo{height:268px}
.tile .bar{height:61px;background:var(--green);color:var(--white);font-family:"Roboto",Arial,sans-serif;font-weight:700;font-size:17px;padding:20px 28px;display:flex;justify-content:space-between;align-items:center;letter-spacing:.5px}

/* news */
.news{width:265px;background:var(--white);border:1px solid var(--line);text-align:center;box-shadow:0 2px 6px rgba(0,0,0,.06)}
.news .photo{height:220px;position:relative}
.news .date{position:absolute;left:113px;top:193px;width:40px;height:40px;border-radius:50%;background:var(--green);border:2px solid var(--white);color:var(--white);font-size:9px;line-height:11px;padding-top:8px}
.news h4{font-size:14.5px;color:var(--ink);font-weight:700;line-height:22px;margin:38px 10px 0}
.news p{font-size:13px;line-height:20px;margin:12px 24px 0;color:#666}

/* testimonial */
.quote-mark{font-family:Georgia,serif;font-size:40px;color:var(--green);font-weight:700;line-height:0;vertical-align:-12px;margin-right:8px}

/* partners */
.partner{width:174px;height:90px;background:#efefef}
.partner span{position:absolute;left:47px;top:33px;width:80px;height:24px;border-radius:3px;background:#c6c6c6}

/* footer */
.footer{left:0;top:4553px;width:1200px;height:464px;background:var(--green);color:var(--white)}
.footer h5{position:absolute;top:72px;font-family:"Roboto",Arial,sans-serif;font-size:22px;font-weight:500}
.footer .small{font-size:12px;line-height:24px}
.field{position:absolute;left:467px;width:352px;border:1px solid rgba(255,255,255,.85);font-size:10px;padding:10px 12px}
.circle-icon{width:34px;height:34px;border-radius:50%;border:2px solid var(--white)}
</style>
</head>
<body>

<!-- top bar -->
<div class="abs topbar">
  <div class="abs social" style="left:140px"></div>
  <div class="abs social" style="left:175px"></div>
  <div class="abs social" style="left:210px"></div>
  <div class="abs divider" style="left:570px"></div>
  <svg class="abs" style="left:590px;top:12px" width="16" height="16" viewBox="0 0 24 24"><path fill="#fff" d="M6.6 10.8a15 15 0 0 0 6.6 6.6l2.2-2.2c.3-.3.7-.4 1-.2 1.1.4 2.3.6 3.6.6.6 0 1 .4 1 1V20c0 .6-.4 1-1 1A17 17 0 0 1 3 4c0-.6.4-1 1-1h3.5c.6 0 1 .4 1 1 0 1.3.2 2.5.6 3.6.1.3 0 .7-.2 1z"/></svg>
  <div class="abs info" style="left:624px">Call: (888) 888-8888</div>
  <div class="abs divider" style="left:790px"></div>
  <svg class="abs" style="left:815px;top:12px" width="18" height="16" viewBox="0 0 24 20"><rect x="2" y="2" width="20" height="16" rx="2" fill="none" stroke="#fff" stroke-width="2"/><path d="M2 4l10 7 10-7" fill="none" stroke="#fff" stroke-width="2"/></svg>
  <div class="abs info" style="left:856px">Email : info@greenmore.example</div>
</div>

<!-- header -->
<div class="abs header">
  <div class="abs brand-dot" style="left:146px;top:32px"></div>
  <div class="abs brand" style="left:172px;top:14px">Greenmore</div>
  <nav class="nav">
    <a class="active" style="left:428px">HOME</a>
    <a style="left:510px">ABOUT US</a>
    <a style="left:623px">SERVICES</a>
    <a style="left:729px">BLOG</a>
    <a style="left:808px">CONTACT</a>
  </nav>
  <div class="abs btn-outline" style="left:899px;top:18px;width:162px;height:46px;line-height:42px">GET A QUOTE</div>
</div>

<!-- hero -->
<div class="abs hero" role="img" aria-label="Business team of four colleagues talking around an office table">
  <div class="abs heading hero-title">GREENMORE</div>
  <div class="abs hero-sub">Sed ut perspiciatis unde omnis iste natus error sit voluptatem<br>accusantium doloremque</div>
  <div class="abs btn-solid" style="left:526px;top:215px;width:175px;height:46px;line-height:46px">GET STARTED</div>
  <svg class="abs" style="left:88px;top:260px" width="20" height="44"><path d="M17 2L3 22l14 20" fill="none" stroke="#fff" stroke-width="2"/></svg>
  <svg class="abs" style="left:1074px;top:260px" width="20" height="44"><path d="M3 2l14 20L3 42" fill="none" stroke="#fff" stroke-width="2"/></svg>
  <div class="abs dot" style="left:560px;top:555px"></div>
  <div class="abs dot" style="left:582px;top:555px"></div>
  <div class="abs dot" style="left:604px;top:555px;background:#fff"></div>
  <div class="abs dot" style="left:626px;top:555px"></div>
</div>

<!-- services -->
<div class="abs heading section-title" style="top:798px">OUR SERVICES</div>
<div class="abs underline" style="top:860px"></div>

<div class="abs service" style="left:108px;top:909px">
  <div class="ring"><div class="core" role="img" aria-label="Handshake icon"></div></div>
  <h3>NEQUE QUISQUAM</h3>
  <p>Sed ut perspiciatis unde omnis istor sit voluptatem accusantium doloremque laudantium, totam rem aperiam, eaque ipsa quae inventore</p>
</div>
<div class="abs service" style="left:356px;top:909px">
  <div class="ring"><div class="core" role="img" aria-label="Signed document icon"></div></div>
  <h3>NEQUE QUISQUAM</h3>
  <p>Sed ut perspiciatis unde omnis istor sit voluptatem accusantium doloremque laudantium, totam rem aperiam, eaque ipsa quae inventore</p>
</div>
<div class="abs service" style="left:604px;top:909px">
  <div class="ring"><div class="core" role="img" aria-label="Presenter at a desk icon"></div></div>
  <h3>NEQUE QUISQUAM</h3>
  <p>Sed ut perspiciatis unde omnis istor sit voluptatem accusantium doloremque laudantium, totam rem aperiam, eaque ipsa quae inventore</p>
</div>
<div class="abs service" style="left:852px;top:909px">
  <div class="ring"><div class="core" role="img" aria-label="Worker with tools icon"></div></div>
  <h3>NEQUE QUISQUAM</h3>
  <p>Sed ut perspiciatis unde omnis istor sit voluptatem accusantium doloremque laudantium, totam rem aperiam, eaque ipsa quae inventore</p>
</div>
<div class="abs btn-outline" style="left:161px;top:1247px;width:135px;height:36px;line-height:32px">READ MORE</div>
<div class="abs btn-outline" style="left:409px;top:1247px;width:135px;height:36px;line-height:32px">READ MORE</div>
<div class="abs btn-outline" style="left:657px;top:1247px;width:135px;height:36px;line-height:32px">READ MORE</div>
<div class="abs btn-outline" style="left:905px;top:1247px;width:135px;height:36px;line-height:32px">READ MORE</div>

<!-- welcome -->
<div class="abs" style="left:127px;top:1384px;font-family:Roboto,sans-serif;font-size:28px;color:var(--green)">WELCOME TO</div>
<div class="abs" style="left:127px;top:1412px;font-family:Roboto,sans-serif;font-size:50px;color:var(--ink)">GREENMORE</div>
<div class="abs" style="left:127px;top:1480px;width:60px;height:2px;background:var(--ink)"></div>
<p class="abs" style="left:127px;top:1504px;width:495px;font-size:13.5px;line-height:26.3px;color:#555">Sed ut perspiciatis unde omnis iste natus error sit voluptatem accusantium doloremque laudantium, totam rem aperiam, eaque ab inventore veritatis et quasi architecto beatae vitae dicta sunt explicabom ipsam voluptatem quia voluptas sit aspernatudit aut fugit, sed quia consequumagni dolores eos qui ratione voluptatem sequi nesciunt. Neque porro quisquam est, qui dolorem ipsum quia dolor sit amet, consectetur, adipisci velit, sed quia non numquam eius modi &nbsp;mpora incidunt ut labore et dolore magnam quasi architecto beatae vitae dicta sunt explicabo.</p>
<div class="abs btn-outline" style="left:127px;top:1740px;width:164px;height:42px;line-height:38px">LEARN MORE</div>
<div class="abs" style="left:672px;top:1432px;width:382px;height:403px;border-left:2px solid var(--green);border-bottom:2px solid var(--green)"></div>
<div class="abs" style="left:688px;top:1375px;width:512px;height:446px;background:linear-gradient(120deg,#5d6d7e,#b4b0a8 50%,#7a8a96)" role="img" aria-label="Smiling colleagues in a meeting around a laptop"></div>

<!-- industry -->
<div class="abs heading section-title" style="top:1932px">INDUSTRY WE SERVE</div>
<div class="abs underline" style="top:1994px"></div>

<div class="abs tile" style="left:134px;top:2036px"><div class="photo" style="background:linear-gradient(135deg,#a89a86,#d8d2c8)" role="img" aria-label="Two women reviewing notes at home"></div><div class="bar">FINIBUS BONORUM <svg width="28" height="14"><path d="M0 7h26M20 1l6 6-6 6" fill="none" stroke="#fff" stroke-width="2"/></svg></div></div>
<div class="abs tile" style="left:454px;top:2036px"><div class="photo" style="background:linear-gradient(135deg,#8f7a63,#cfc7b8)" role="img" aria-label="Team workshop in front of a sticky-note board"></div><div class="bar">FINIBUS BONORUM <svg width="28" height="14"><path d="M0 7h26M20 1l6 6-6 6" fill="none" stroke="#fff" stroke-width="2"/></svg></div></div>
<div class="abs tile" style="left:773px;top:2036px"><div class="photo" style="background:linear-gradient(135deg,#6f8195,#c8ccd0)" role="img" aria-label="Two businessmen reviewing a chart"></div><div class="bar">FINIBUS BONORUM <svg width="28" height="14"><path d="M0 7h26M20 1l6 6-6 6" fill="none" stroke="#fff" stroke-width="2"/></svg></div></div>
<div class="abs tile" style="left:134px;top:2396px"><div class="photo" style="background:linear-gradient(135deg,#7b6a58,#bdb3a4)" role="img" aria-label="Two women laughing at a laptop"></div><div class="bar">FINIBUS BONORUM <svg width="28" height="14"><path d="M0 7h26M20 1l6 6-6 6" fill="none" stroke="#fff" stroke-width="2"/></svg></div></div>
<div class="abs tile" style="left:454px;top:2396px"><div class="photo" style="background:linear-gradient(135deg,#6b6a66,#c9bfae)" role="img" aria-label="Man and woman looking at a tablet"></div><div class="bar">FINIBUS BONORUM <svg width="28" height="14"><path d="M0 7h26M20 1l6 6-6 6" fill="none" stroke="#fff" stroke-width="2"/></svg></div></div>
<div class="abs tile" style="left:773px;top:2396px"><div class="photo" style="background:linear-gradient(135deg,#cfd4d0,#5b6673)" role="img" aria-label="Two men talking at an office desk"></div><div class="bar">FINIBUS BONORUM <svg width="28" height="14"><path d="M0 7h26M20 1l6 6-6 6" fill="none" stroke="#fff" stroke-width="2"/></svg></div></div>

<!-- testimonial -->
<div class="abs" style="left:0;top:2821px;width:1200px;height:506px;background:linear-gradient(90deg,#3fa052,#55ad63 50%,#3c9b4e)" role="img" aria-label="Green-tinted photo of a business meeting"></div>
<svg class="abs" style="left:158px;top:3025px" width="22" height="36"><path d="M19 2L4 18l15 16" fill="none" stroke="#fff" stroke-width="3"/></svg>
<svg class="abs" style="left:968px;top:3025px" width="22" height="36"><path d="M3 2l15 16L3 34" fill="none" stroke="#fff" stroke-width="3"/></svg>
<div class="abs" style="left:240px;top:2920px;width:668px;height:275px;background:var(--white);border-radius:6px;box-shadow:0 3px 10px rgba(0,0,0,.15)"></div>
<p class="abs" style="left:314px;top:2961px;width:522px;text-align:center;font-size:15px;line-height:26.5px;color:#444"><span class="quote-mark">&ldquo;</span>Nemo enim ipsam voluptatem quia voluptas sit aspernatur aut odit aut fugit, sed quia consequuntur magni dolores eos qui ratione voluptatem sequi nesciunt. Neque porro quisquam est, qui dolorem ipsum quia dolor sit amet, consectetur</p>
<div class="abs" style="left:485px;top:3085px;font-size:13px;color:#444">Daniel Reyes &ndash; &nbsp;Mmnis iste</div>
<div class="abs" style="left:698px;top:3068px;font-family:Georgia,serif;font-size:44px;color:var(--green);font-weight:700">&rdquo;</div>
<div class="abs" style="left:438px;top:3151px;width:80px;height:80px;border-radius:50%;border:4px solid var(--white);background:#9aa6b0" role="img" aria-label="Client portrait"></div>
<div class="abs" style="left:522px;top:3129px;width:108px;height:108px;border-radius:50%;border:5px solid var(--white);background:#b3aea6" role="img" aria-label="Featured client portrait"></div>
<div class="abs" style="left:634px;top:3151px;width:80px;height:80px;border-radius:50%;border:4px solid var(--white);background:#8a9aa3" role="img" aria-label="Client portrait"></div>

<!-- latest news -->
<div class="abs" style="left:0;top:3327px;width:1200px;height:745px;background:var(--light)"></div>
<div class="abs heading section-title" style="top:3405px">LATEST NEWS</div>
<div class="abs underline" style="top:3468px"></div>

<div class="abs news" style="left:156px;top:3518px;height:436px">
  <div class="photo" style="background:linear-gradient(135deg,#8d98a2,#d5d2cc)" role="img" aria-label="Man and woman discussing at a desk"><div class="date">AUG<br>2021</div></div>
  <h4>Nemo enim ipsam voluptatem<br>quia voluptas asperatur</h4>
  <p>Sed ut perspiciatis unde omnis iste natus voluptatem accusantium dolue laudantium, totam</p>
  <div class="btn-outline" style="width:136px;height:38px;line-height:34px;margin:20px auto 0;font-size:13px">READ MORE</div>
</div>
<div class="abs news" style="left:468px;top:3536px;height:432px">
  <div class="photo" style="background:linear-gradient(135deg,#6d747c,#c4c0b8)" role="img" aria-label="Colleagues working together on laptops"><div class="date">AUG<br>2021</div></div>
  <h4>Nemo enim ipsam voluptatem<br>quia voluptas asperatur</h4>
  <p>Sed ut perspiciatis unde omnis iste natus voluptatem accusantium dolue laudantium, totam</p>
  <div class="btn-outline" style="width:136px;height:38px;line-height:34px;margin:20px auto 0;font-size:13px">READ MORE</div>
</div>
<div class="abs news" style="left:779px;top:3518px;height:436px">
  <div class="photo" style="background:linear-gradient(135deg,#6c7d8a,#cfd3d2)" role="img" aria-label="Team standing in a bright office"><div class="date">AUG<br>2021</div></div>
  <h4>Nemo enim ipsam voluptatem<br>quia voluptas asperatur</h4>
  <p>Sed ut perspiciatis unde omnis iste natus voluptatem accusantium dolue laudantium, totam</p>
  <div class="btn-outline" style="width:136px;height:38px;line-height:34px;margin:20px auto 0;font-size:13px">READ MORE</div>
</div>

<!-- partners -->
<div class="abs heading section-title" style="top:4147px">GREENMORE PARTNERS</div>
<div class="abs underline" style="top:4210px"></div>
<div class="abs partner" style="left:138px;top:4260px"><span></span></div>
<div class="abs partner" style="left:325px;top:4260px"><span></span></div>
<div class="abs partner" style="left:513px;top:4260px"><span></span></div>
<div class="abs partner" style="left:701px;top:4260px"><span></span></div>
<div class="abs partner" style="left:888px;top:4260px"><span></span></div>
<div class="abs partner" style="left:232px;top:4365px"><span></span></div>
<div class="abs partner" style="left:419px;top:4365px"><span></span></div>
<div class="abs partner" style="left:606px;top:4365px"><span></span></div>
<div class="abs partner" style="left:794px;top:4365px"><span></span></div>

<!-- footer -->
<div class="abs footer">
  <h5 style="left:156px">CONTACT US</h5>
  <h5 style="left:467px">REQUEST A QUOTE</h5>
  <h5 style="left:900px">QUICK LINKS</h5>

  <svg class="abs" style="left:156px;top:141px" width="14" height="18" viewBox="0 0 14 18"><path d="M7 1a6 6 0 0 0-6 6c0 4.5 6 10 6 10s6-5.5 6-10a6 6 0 0 0-6-6z" fill="none" stroke="#fff" stroke-width="1.6"/><circle cx="7" cy="7" r="2" fill="#fff"/></svg>
  <div class="abs small" style="left:188px;top:130px;width:230px">Greenmore<br>48 Harbor Lane Springvale USA<br>20418</div>
  <svg class="abs" style="left:156px;top:211px" width="14" height="14" viewBox="0 0 24 24"><path fill="none" stroke="#fff" stroke-width="2" d="M6.6 10.8a15 15 0 0 0 6.6 6.6l2.2-2.2 4.6 1.1V20A17 17 0 0 1 3 4h3.5l1.1 4.6z"/></svg>
  <div class="abs small" style="left:188px;top:206px">Phone:(888) 888 8888</div>
  <svg class="abs" style="left:156px;top:244px" width="14" height="14" viewBox="0 0 14 14"><rect x="1" y="4" width="12" height="8" fill="none" stroke="#fff" stroke-width="1.4"/><rect x="3" y="1" width="8" height="4" fill="none" stroke="#fff" stroke-width="1.4"/></svg>
  <div class="abs small" style="left:188px;top:239px">Fax: 888 888 8888</div>
  <svg class="abs" style="left:156px;top:277px" width="16" height="12" viewBox="0 0 16 12"><rect x="1" y="1" width="14" height="10" fill="none" stroke="#fff" stroke-width="1.4"/><path d="M1 1l7 5 7-5" fill="none" stroke="#fff" stroke-width="1.4"/></svg>
  <div class="abs small" style="left:188px;top:271px">Email: info@greenmore.example</div>

  <div class="field" style="top:124px;height:38px">Your Name</div>
  <div class="field" style="top:172px;height:38px">Email Address</div>
  <div class="field" style="top:220px;height:60px">Message</div>
  <div class="abs" style="left:467px;top:294px;width:154px;height:36px;border:2px solid #fff;border-radius:20px;text-align:center;line-height:32px;font-size:14px;font-weight:600">SUBMIT</div>

  <div class="abs small" style="left:900px;top:124px;line-height:26.5px">Home<br>About<br>Services<br>Blog<br>Contact Us</div>

  <div class="abs" style="left:0;top:354px;width:1200px;height:1px;background:rgba(255,255,255,.3)"></div>
  <div class="abs brand-dot" style="left:156px;top:402px;background:#fff"></div>
  <div class="abs brand" style="left:182px;top:382px;color:#fff">Greenmore</div>
  <div class="abs" style="left:172px;top:430px;font-size:8px">Business Consulting from Startup to Exit</div>
  <div class="abs small" style="left:482px;top:396px">&copy;Copyright @2021 Greenmore . All Rights Reserved.</div>
  <div class="abs circle-icon" style="left:872px;top:391px"></div>
  <div class="abs circle-icon" style="left:919px;top:391px"></div>
  <div class="abs circle-icon" style="left:966px;top:391px"></div>
  <div class="abs circle-icon" style="left:1013px;top:391px"></div>
</div>

</body>
</html>
```